KEV.PRO- Darren Holcombe Fitness- needs a clever business card using the logo, name, info, contact

I need a business card designed for my Online Personal Training company called KEV.PRO, abbreviation for Darren Holcombe Fitness. My company focuses on coaching in personal health and personal growth to unleash your greatest potential. I would like to see designs that use my color scheme of a redish-orange (C:0,M:84,Y:100,K:0), grey, white, black, and my company font is OSWALD. The final design should communicate some aspects of design, health, motivation, growth, in some way. The logo is very important to the company and can be displayed in any of the colors previously mentioned. Must include the company name, my website: www.kev-pro.example , my email: dan@kev-pro.example

Target Market(s)

Personal health, fitness, general public, those who lack knowledge, awareness, and confidence in personal health

Industry/Entity Type

Personal Trainer

Font styles to use
Other font styles liked:
• OSWALD. (Bold, Regular, Light)

Colors
f37122
ffffff
9d9d9d
000000

Requirements
Must have
• Must include the logo, company name, my website: www.kev-pro.example , my email: dan@kev-pro.example
Nice to have
• Variations of the colors scheme of a redish-orange (C:0,M:84,Y:100,K:0), grey, white, black. Logo, card, or text can be in any of these colors.
• Possible quote like "Take control of your personal health to unleash your greatest potential" or "Unleashing your greatness first begins with fitness of the body and mind"

```html
<!DOCTYPE html>
<html lang="en">
<head>
<meta charset="utf-8">
<title>KEV.PRO business card</title>
<link href="https://fonts.googleapis.com/css2?family=Oswald:wght@400&family=Montserrat:wght@300&family=Roboto:wght@300;400&display=swap" rel="stylesheet">
<style>
  :root {
    --orange: #f04f23;
    --orange-deep: #e2461c;
    --white: #ffffff;
    --grey: #9d9d9d;
    --ink: #1e1e1e;
    --stage: #161616;
  }
  * { margin: 0; padding: 0; box-sizing: border-box; }
  html, body { width: 1200px; height: 963px; overflow: hidden; background: var(--stage); }
  .sheet { position: relative; width: 1200px; height: 963px; }
  .card {
    position: absolute; left: 250px; width: 700px; height: 400px;
    border-radius: 22px; overflow: hidden;
  }
  .card--front { top: 60px; background: var(--white); }
  .card--back { top: 503px; background: var(--orange); }

  /* front */
  .person { position: absolute; left: 52px; top: 52px; }
  .person__name {
    font-family: "Montserrat", sans-serif; font-weight: 300;
    font-size: 27px; letter-spacing: 4px; color: var(--orange); text-transform: uppercase;
  }
  .person__role { font-family: "Roboto", sans-serif; font-size: 15px; color: var(--ink); margin-top: 2px; }
  .rule { position: absolute; left: 52px; right: 52px; top: 128px; height: 1.5px; background: var(--orange); }
  .contact { position: absolute; left: 52px; top: 146px; list-style: none;
    font-family: "Roboto", sans-serif; font-weight: 300; font-size: 15px; color: var(--ink); line-height: 22px; }
  .contact li { display: flex; align-items: center; gap: 10px; }
  .contact svg { width: 10px; height: 10px; flex: none; }
  .address { position: absolute; right: 52px; top: 146px; text-align: right; font-style: normal;
    font-family: "Roboto", sans-serif; font-weight: 300; font-size: 15px; color: var(--ink); line-height: 22px; }

  .brand { position: absolute; display: flex; align-items: center; gap: 12px; }
  .brand__dot { border-radius: 50%; flex: none; }
  .brand__name { font-family: "Roboto", sans-serif; font-weight: 400; line-height: 1; letter-spacing: 3px; }
  .card--front .brand { right: 52px; top: 58px; }
  .card--front .brand__dot { width: 18px; height: 18px; background: var(--orange); }
  .card--front .brand__name { font-size: 24px; color: var(--ink); }

  .base-band { position: absolute; left: 0; right: 0; bottom: 0; height: 18px; background: var(--orange); }

  /* back */
  .card--back .brand { left: 330px; top: 150px; }
  .card--back .brand__dot { width: 24px; height: 24px; background: var(--white); }
  .card--back .brand__name { font-size: 36px; color: var(--white); }
  .backdrop-disc { position: absolute; right: -90px; bottom: -150px; width: 380px; height: 380px;
    border-radius: 50%; background: var(--orange-deep); }
  .tagline { position: absolute; left: 52px; bottom: 62px;
    font-family: "Oswald", sans-serif; font-weight: 400; font-size: 21px; letter-spacing: .5px; color: var(--white); }
</style>
</head>
<body>
<main class="sheet">
  <section class="card card--front" aria-label="Business card front">
    <div class="person">
      <h1 class="person__name">Dan Holcombe</h1>
      <p class="person__role">Trainer</p>
    </div>
    <div class="brand">
      <span class="brand__dot"></span>
      <span class="brand__name">KEV.PRO</span>
    </div>
    <div class="rule"></div>
    <ul class="contact">
      <li><svg viewBox="0 0 10 10"><path d="M2 1h2l1 2-1.2 1a6 6 0 0 0 2.2 2.2L7 5l2 1v2a1 1 0 0 1-1 1A7 7 0 0 1 1 2a1 1 0 0 1 1-1z" fill="var(--orange)"/></svg>+1 555 010 2284</li>
      <li><svg viewBox="0 0 10 10"><rect x="0.5" y="2" width="9" height="6.5" fill="none" stroke="var(--orange)"/><path d="M0.5 2 5 5.5 9.5 2" fill="none" stroke="var(--orange)"/></svg>dan@kev-pro.example</li>
      <li><svg viewBox="0 0 10 10"><circle cx="5" cy="5" r="4.3" fill="none" stroke="var(--orange)"/><path d="M0.7 5h8.6M5 .7c-2 2.5-2 6.1 0 8.6M5 .7c2 2.5 2 6.1 0 8.6" fill="none" stroke="var(--orange)" stroke-width=".8"/></svg>www.kev-pro.example</li>
    </ul>
    <address class="address">418 Birchwood Ave<br>Denver, CO 80205</address>
    <div class="base-band"></div>
  </section>

  <section class="card card--back" aria-label="Business card back">
    <div class="backdrop-disc"></div>
    <div class="brand">
      <span class="brand__dot"></span>
      <span class="brand__name">KEV.PRO</span>
    </div>
    <p class="tagline">Take control of your personal health to unleash your greatest potential</p>
  </section>
</main>
</body>
</html>
```